Wren Vehicle Polishing (Mobile detail)

I need a business card made up. I'd like it to be different in some form, either raised, embossed, debossed, something cool that stands out. (preferably embossed text somewhere in it). I will be including the Initial png file. Let me know if you need the photoshop of adobe illustrator file to work with.

Information to be included: Text: XXX-XXX-XXXX Phone: XXX-XXX-XXXX Email: wrenpolishcrew@mailbox-demo.net Website: www.socialpage-demo.net/wrenpolishKTR Hours of operation: Mon - Fri 7:00AM to 8:00PM Sat - 10:00AM to 8:00PM

Target Market(s)

Mobile automotive detailing

Industry/Entity Type

Automotive

Contact Information for Business Card

Make it stand out with embossed lettering, I'd also like the background to be glossy black or matte, something that represents a shiny car, black preferred

Requirements
Must have
• A glossy background, or something.
• My logo, pick one of them that best fits your design.
Should not have
• White background,
• something that does not stand out.

```html
<!DOCTYPE html>
<html lang="en">
<head>
<meta charset="UTF-8">
<title>Wren Vehicle Polishing – Business Card</title>
<link href="https://fonts.googleapis.com/css2?family=Open+Sans:wght@400;600;700&display=swap" rel="stylesheet">
<style>
  :root {
    --stage: #3a3b3d;
    --card-black: #0d0d0e;
    --card-gloss: #2a2b2d;
    --accent: #ef4a1f;
    --silver: #d9dbde;
    --silver-dark: #8d9095;
    --text-light: #ffffff;
    --text-muted: #a9abaf;
  }
  * { box-sizing: border-box; margin: 0; padding: 0; }
  html, body {
    width: 1200px; height: 950px; overflow: hidden;
    background: var(--stage);
    font-family: "Open Sans", Arial, sans-serif;
  }
  .sheet {
    position: relative; width: 1200px; height: 950px;
  }
  .card {
    position: absolute; left: 260px; width: 680px; height: 388px;
    border-radius: 4px; overflow: hidden;
    background:
      linear-gradient(115deg, transparent 0 55%, rgba(255,255,255,0.10) 62%, transparent 70%),
      linear-gradient(160deg, var(--card-gloss) 0%, var(--card-black) 55%, #050505 100%);
    box-shadow: 0 10px 24px rgba(0,0,0,0.45);
  }
  .card--back { top: 60px; }
  .card--front { top: 502px; }

  /* brand lockup */
  .brand {
    position: absolute; display: flex; align-items: center; gap: 14px;
  }
  .brand__dot {
    width: 46px; height: 46px; border-radius: 50%;
    background: var(--accent);
  }
  .brand__name {
    font-weight: 700; font-size: 27px; line-height: 1.1;
    color: var(--silver); width: 200px;
  }
  .card--back .brand { left: 50%; top: 92px; transform: translateX(-50%); }
  .card--front .brand { left: 410px; top: 150px; }

  /* hours */
  .hours {
    position: absolute; left: 0; right: 0; top: 236px; text-align: center;
  }
  .hours__title {
    color: var(--accent); font-weight: 700; font-size: 17px; letter-spacing: 0.5px;
  }
  .hours__line {
    color: var(--text-muted); font-size: 15px; margin-top: 6px;
  }

  /* front side */
  .front-panel { position: absolute; inset: 0; }
  .contact {
    position: absolute; left: 30px; top: 92px; color: var(--text-light);
  }
  .contact__name { font-weight: 700; font-size: 21px; }
  .contact__role { font-size: 15px; margin-bottom: 16px; }
  .contact__list { list-style: none; }
  .contact__item {
    display: flex; align-items: center; gap: 9px;
    font-size: 15px; line-height: 1.65; white-space: nowrap;
  }
  .contact__item--small { font-size: 11.5px; }
  .icon { width: 14px; height: 14px; flex: none; fill: var(--text-light); }
</style>
</head>
<body>
<main class="sheet">

  <section class="card card--back" aria-label="Card back">
    <div class="brand">
      <span class="brand__dot"></span>
      <span class="brand__name">Wren Vehicle Polishing</span>
    </div>
    <div class="hours">
      <p class="hours__title">HOURS OF OPERATION</p>
      <p class="hours__line">Mon - Fri 7:00AM to 8:00PM</p>
      <p class="hours__line">Sat - 10:00AM to 8:00PM</p>
    </div>
  </section>

  <section class="card card--front" aria-label="Card front">
    <svg class="front-panel" viewBox="0 0 680 388" width="680" height="388" aria-hidden="true">
      <defs>
        <linearGradient id="silverEdge" x1="0" y1="0" x2="0" y2="1">
          <stop offset="0" stop-color="#6f7277"/>
          <stop offset="0.45" stop-color="#f4f5f6"/>
          <stop offset="1" stop-color="#7c7f84"/>
        </linearGradient>
      </defs>
      <path d="M0 0 H212 C318 80 328 290 240 388 H0 Z" fill="url(#silverEdge)" transform="translate(10 0)"/>
      <path d="M0 0 H212 C318 80 328 290 240 388 H0 Z" fill="var(--accent)"/>
    </svg>

    <div class="contact">
      <p class="contact__name">Milo Grant</p>
      <p class="contact__role">Detailer</p>
      <ul class="contact__list">
        <li class="contact__item">
          <svg class="icon" viewBox="0 0 14 14"><rect x="3" y="0" width="8" height="14" rx="1.5"/><rect x="4.5" y="2" width="5" height="8" fill="var(--accent)"/></svg>
          555-014-2290
        </li>
        <li class="contact__item">
          <svg class="icon" viewBox="0 0 14 14"><path d="M1 5 C1 2 13 2 13 5 L11 6 L10 4 H4 L3 6 Z"/><rect x="2" y="7" width="10" height="6" rx="1"/></svg>
          555-017-8813
        </li>
        <li class="contact__item contact__item--small">
          <svg class="icon" viewBox="0 0 14 14"><rect x="0" y="2" width="14" height="10" rx="1"/><path d="M0.5 2.5 L7 8 L13.5 2.5" stroke="var(--accent)" stroke-width="1.4" fill="none"/></svg>
          wrenpolishcrew@mailbox-demo.net
        </li>
        <li class="contact__item contact__item--small">
          <svg class="icon" viewBox="0 0 14 14"><rect x="1" y="1" width="12" height="12" rx="2"/></svg>
          www.socialpage-demo.net/wrenpolishKTR
        </li>
      </ul>
    </div>

    <div class="brand">
      <span class="brand__dot"></span>
      <span class="brand__name">Wren Vehicle Polishing</span>
    </div>
  </section>

</main>
</body>
</html>
```